Brambleway Foundation Brochure

We are looking for a new brochure design for our foundation. The foundation is a nonprofit organization that provides assistance to special needs families in Indiana. We do this by providing ipads, communication software, gas cards, and financial assistance to families for their special needs child.

Target Market(s)

Families

Industry/Entity Type

Foundation

Colors
0355a3
3176b5
34a6d7
9bcb3b

Requirements
Must have
• Clear concise information

```html
<!DOCTYPE html>
<html lang="en">
<head>
<meta charset="utf-8">
<title>Brambleway Foundation Brochure</title>
<link href="https://fonts.googleapis.com/css2?family=Josefin+Sans:ital,wght@0,400;0,600;0,700;1,600;1,700&family=Cinzel:wght@500&display=swap" rel="stylesheet">
<style>
  :root {
    --navy: #0355a3;
    --mid-blue: #3176b5;
    --sky: #34a6d7;
    --lime: #9bcb3b;
    --ink: #2b2f36;
    --paper: #ffffff;
    --stage: #ebe8e3;
  }
  * { margin: 0; padding: 0; box-sizing: border-box; }
  html, body { width: 1200px; height: 1200px; overflow: hidden; }
  body {
    background: var(--stage);
    font-family: "Josefin Sans", sans-serif;
    color: var(--ink);
    position: relative;
  }
  .spread {
    position: absolute;
    width: 760px;
    height: 575px;
    background: var(--paper);
    box-shadow: 0 6px 18px rgba(0,0,0,.18);
    overflow: hidden;
  }
  .spread--outside { left: 380px; top: 15px; }
  .spread--inside { left: 60px; top: 608px; }
  .spread > svg { position: absolute; inset: 0; width: 760px; height: 575px; }
  .fold {
    position: absolute; top: 0; bottom: 0; width: 1px;
    background: rgba(0,0,0,.06);
  }
  .block { position: absolute; }

  .heading {
    font-weight: 700; font-style: italic; color: var(--mid-blue);
    line-height: 1.1;
  }
  .body-copy {
    font-size: 9px; line-height: 1.5; text-align: justify;
  }

  /* Outside */
  .story { left: 22px; top: 200px; width: 212px; }
  .story .heading { font-size: 20px; text-align: right; margin-bottom: 8px; }
  .signature { text-align: right; margin-top: 10px; font-size: 9px; line-height: 1.35; }
  .signature strong { font-size: 12px; font-style: italic; color: var(--ink); display: block; }

  .org-name {
    font-family: "Josefin Sans", sans-serif;
    font-weight: 600; color: var(--navy);
    display: flex; align-items: center; gap: 6px;
  }
  .org-name .dot { width: 10px; height: 10px; border-radius: 50%; background: var(--lime); flex: none; }
  .back-logo { left: 283px; top: 290px; width: 200px; font-size: 17px; line-height: 1.1; }
  .contacts { left: 283px; top: 372px; width: 210px; font-size: 10px; line-height: 1.6; }
  .contacts li { list-style: none; display: flex; align-items: center; gap: 6px; }
  .contacts svg { width: 11px; height: 11px; flex: none; }
  .contacts .address { margin-top: 8px; padding-top: 6px; border-top: 1px solid var(--mid-blue); align-items: flex-start; }

  .cover-logo { left: 662px; top: 42px; width: 86px; font-size: 11px; line-height: 1.1; }
  .tagline {
    left: 532px; top: 400px; width: 220px;
    font-family: "Cinzel", serif; font-weight: 500;
    color: #fff; font-size: 15px; line-height: 1.45; letter-spacing: .5px;
  }
  .cover-url {
    left: 560px; top: 528px; width: 190px; text-align: right;
    color: #fff; font-size: 10px; letter-spacing: 4px;
  }

  /* Inside */
  .what { left: 22px; top: 365px; width: 215px; color: #fff; }
  .what .heading { color: #fff; font-size: 19px; margin-bottom: 8px; }
  .what .body-copy { font-size: 9.5px; }

  .difference { left: 562px; top: 26px; width: 183px; }
  .difference .heading { font-size: 16px; }
  .lead { font-weight: 700; font-style: italic; font-size: 10px; line-height: 1.35; margin: 4px 0 6px; }
  .bullets { list-style: none; font-size: 9px; line-height: 1.6; }
  .bullets li { display: flex; align-items: baseline; gap: 6px; }
  .bullets li::before {
    content: ""; width: 5px; height: 5px; border-radius: 50%;
    background: var(--mid-blue); flex: none; transform: translateY(-1px);
  }
  .rule { height: 1px; background: var(--mid-blue); margin: 8px 0 8px; }
  .help .heading { font-size: 16px; margin-bottom: 5px; }
  .help .body-copy a { color: var(--mid-blue); text-decoration: none; }

  .grant { left: 576px; top: 394px; width: 172px; }
  .grant .heading { font-size: 12px; color: var(--navy); line-height: 1.18; margin-bottom: 6px; }
  .grant .bullets { font-size: 8.5px; line-height: 1.45; }
  .grant .bullets li::before { background: var(--navy); }
</style>
</head>
<body>

<section class="spread spread--outside" aria-label="Brochure outside">
  <svg viewBox="0 0 760 575">
    <defs>
      <linearGradient id="fenceTones" x1="0" y1="0" x2="1" y2="1">
        <stop offset="0" stop-color="#7d9a6a"/>
        <stop offset=".5" stop-color="#3f5140"/>
        <stop offset="1" stop-color="#8e9a86"/>
      </linearGradient>
      <linearGradient id="familyTones" x1="0" y1="0" x2="1" y2="0">
        <stop offset="0" stop-color="#4d6a48"/>
        <stop offset=".3" stop-color="#c4584e"/>
        <stop offset=".55" stop-color="#3a3a3c"/>
        <stop offset=".8" stop-color="#d9b8a3"/>
        <stop offset="1" stop-color="#e06a9a"/>
      </linearGradient>
    </defs>
    <g role="img" aria-label="Photo: iron fence and trees in a park">
      <path d="M0 0H253V118Q130 120 0 175Z" fill="url(#fenceTones)"/>
    </g>
    <g role="img" aria-label="Photo: smiling boy on a swing, and a mother hugging her young daughter">
      <path d="M253 0H760V330Q640 388 525 335Q430 140 253 118Z" fill="url(#familyTones)"/>
    </g>
    <path d="M0 186Q130 128 253 128" fill="none" stroke="#9bcb3b" stroke-width="7"/>
    <path d="M0 197Q130 140 253 139" fill="none" stroke="#3176b5" stroke-width="4"/>
    <path d="M253 128Q432 150 525 345Q640 400 760 342" fill="none" stroke="#9bcb3b" stroke-width="8"/>
    <path d="M506 330Q520 345 528 356Q640 412 760 356V575H506Z" fill="#0355a3"/>
    <path d="M253 139Q430 164 520 356" fill="none" stroke="#3176b5" stroke-width="5"/>
    <path d="M506 520Q630 505 760 475V575H506Z" fill="#3176b5"/>
    <path d="M506 548Q630 535 760 510V575H506Z" fill="#34a6d7"/>
    <circle cx="712" cy="62" r="72" fill="#ffffff"/>
    <path d="M640 62A72 72 0 0 0 760 116" fill="none" stroke="#9bcb3b" stroke-width="5"/>
    <path d="M646 86A72 72 0 0 0 760 128" fill="none" stroke="#3176b5" stroke-width="4"/>
  </svg>
  <div class="fold" style="left:253px"></div>
  <div class="fold" style="left:506px"></div>

  <article class="block story">
    <h2 class="heading">Our Story</h2>
    <p class="body-copy">The Brambleway Families First Foundation was created in 2015 by my wife, Marie, and I, parents of a child with autism. As parents of a special needs child, we understand the unique emotional and financial struggles that come with raising a child who has special needs. Through our personal experience and work with Harborview Autism Center, we saw the overwhelming need in our local community for an organization to provide support to these families who were struggling. It was this recognition of the gap in services for these families that motivated us to create the Brambleway Families First Foundation, an organization dedicated to specifically providing assistance to struggling special needs families. It is through this foundation that we hope to continue to provide hope to special needs families in Northern Indiana.</p>
    <p class="signature"><strong>Daniel Hartwell</strong>Founder, Brambleway<br>Families First Foundation</p>
  </article>

  <div class="block org-name back-logo"><span class="dot"></span><span>Brambleway Families First Foundation</span></div>

  <ul class="block contacts">
    <li><svg viewBox="0 0 12 12"><circle cx="6" cy="6" r="6" fill="#0355a3"/><path d="M4 3.2l1 1.2-.6.8a4 4 0 0 0 2.4 2.4l.8-.6 1.2 1-.6 1C6 9 3 6 3 3.8z" fill="#fff"/></svg>555-201-4478</li>
    <li><svg viewBox="0 0 12 12"><circle cx="6" cy="6" r="6" fill="#0355a3"/><circle cx="6" cy="6" r="2.6" fill="none" stroke="#fff" stroke-width="1"/></svg>www.bwfff.org</li>
    <li><svg viewBox="0 0 12 12"><circle cx="6" cy="6" r="6" fill="#0355a3"/><rect x="3" y="4" width="6" height="4.2" fill="none" stroke="#fff" stroke-width=".9"/><path d="M3 4l3 2.4L9 4" fill="none" stroke="#fff" stroke-width=".9"/></svg>info@bwfff.org</li>
    <li class="address"><svg viewBox="0 0 12 12"><circle cx="6" cy="6" r="6" fill="#0355a3"/><path d="M6 2.5a2.3 2.3 0 0 1 2.3 2.3C8.3 6.6 6 9.5 6 9.5S3.7 6.6 3.7 4.8A2.3 2.3 0 0 1 6 2.5z" fill="#fff"/></svg><span>1840 Alder Creek Drive<br>Fairbrook, IN 46012</span></li>
  </ul>

  <div class="block org-name cover-logo"><span class="dot"></span><span>Brambleway Families First Foundation</span></div>

  <h1 class="block tagline">Providing<br>hope for<br>special needs families</h1>
  <p class="block cover-url">www.bwfff.org</p>
</section>

<section class="spread spread--inside" aria-label="Brochure inside">
  <svg viewBox="0 0 760 575">
    <defs>
      <linearGradient id="limeField" x1="0" y1="0" x2="1" y2="1">
        <stop offset="0" stop-color="#b6d85a"/>
        <stop offset=".6" stop-color="#9bcb3b"/>
        <stop offset="1" stop-color="#6fa02a"/>
      </linearGradient>
      <linearGradient id="founderTones" x1="0" y1="0" x2="1" y2="0">
        <stop offset="0" stop-color="#5a5f62"/>
        <stop offset=".35" stop-color="#c7c38d"/>
        <stop offset=".7" stop-color="#e6dc9a"/>
        <stop offset="1" stop-color="#4a5f86"/>
      </linearGradient>
      <linearGradient id="fadedTones" x1="0" y1="0" x2="1" y2="1">
        <stop offset="0" stop-color="#d9e2ea"/>
        <stop offset="1" stop-color="#eef1f3"/>
      </linearGradient>
    </defs>
    <rect x="0" y="0" width="506" height="575" fill="url(#limeField)"/>
    <g role="img" aria-label="Photo: the founder kneeling beside his son">
      <path d="M28 150Q40 70 140 45L205 0H500V345Q430 405 330 372Q195 330 115 292Q45 255 28 150Z" fill="url(#founderTones)"/>
    </g>
    <path d="M30 95Q70 20 175 25Q150 70 105 92Q60 112 30 95Z" fill="#3176b5"/>
    <path d="M500 330Q430 412 330 382" fill="none" stroke="#3176b5" stroke-width="6"/>
    <g role="img" aria-label="Faded photo: the founder and his son">
      <path d="M575 360Q660 320 760 290V575H555Q595 480 575 360Z" fill="url(#fadedTones)"/>
    </g>
    <path d="M478 0H530Q508 200 556 330Q596 380 760 342V358Q600 400 566 352Q522 460 560 575H452Q512 470 490 330Q470 200 478 0Z" fill="#0355a3"/>
    <path d="M530 0Q508 200 556 330Q596 380 760 342" fill="none" stroke="#34a6d7" stroke-width="4"/>
    <path d="M468 0Q458 200 480 330Q500 450 440 575" fill="none" stroke="#3176b5" stroke-width="7"/>
  </svg>
  <div class="fold" style="left:253px"></div>
  <div class="fold" style="left:506px"></div>

  <article class="block what">
    <h2 class="heading">What we do?</h2>
    <p class="body-copy">The Brambleway Families First Foundation provides assistance to special needs families – in whatever way they may need it. For some families that is easing the financial burden of therapy, for others it is providing an ipad and language software so their nonverbal child can communicate. For others, it may mean providing diapers or clothing or gas cards to drive their children to doctor's appointments. We understand that each family is unique and that means assisting them in different ways, and we are here to do that.</p>
  </article>

  <article class="block difference">
    <h2 class="heading">Making A Difference:</h2>
    <p class="lead">Below are just a few of the children we have assisted through the foundation. We assist families by:</p>
    <ul class="bullets">
      <li>Purchasing ipads</li>
      <li>Purchasing language software</li>
      <li>Providing gas cards</li>
      <li>Providing scholarships for therapy</li>
    </ul>
    <div class="rule"></div>
    <div class="help">
      <h2 class="heading">How can you help?</h2>
      <p class="body-copy">Consider making a donation to the Brambleway Families First Foundation. 100% of proceeds go directly to special needs families in Northern Indiana. You can write a check or visit <a href="#">www.bwfff.org/donate</a> to make a donation online.</p>
    </div>
  </article>

  <article class="block grant">
    <h2 class="heading">Do you have a special needs child?<br>You may qualify for a grant.<br>To find out:</h2>
    <ul class="bullets">
      <li>Visit www.bwfff.org &amp; complete a grant inquiry form</li>
      <li>Complete the entire grant application</li>
      <li>Your application will be reviewed by the foundation &amp; you will be contacted with more information.</li>
    </ul>
  </article>
</section>

</body>
</html>
```